New Wix Website Design Project For New Finance Company

Create new design for a new page. Website should match existing theme of presentation deck, business card and logo attached to the brief. The site will have five pages

1) Home
2) Investment Criteria
3) Approach
4) Team
5) Contact

Some examples include
http://www.bluemaplefunds.com/

Although not a requirement, if the below white fence or similar could be added subtly to the sight as well, that would be great.

https://www.searvok.com/search?q=white+fence+horse&rlz=7K4TTPM_enUS218US264&source=lnms&tbm=isch&sa=X&ved=0bhVKEwqxmbtnyLvgBhWE3oNKHVtsBF4Q_BUIDyhD&biw=1920&bih=958#imgrc=vkd2PQx47eMLTA:

Target Market(s)

Business Professionals

Font styles to use
Sans Serif

Colors

Designer to choose colors to be used in the design.

Requirements
Must have
• Clean layout. Easy to upload header and footer.

```html
<!DOCTYPE html>
<html lang="en">
<head>
<meta charset="utf-8">
<title>Stone Ridge Capital</title>
<link rel="stylesheet" href="https://fonts.googleapis.com/css2?family=Montserrat:wght@400;500;600;700&family=Open+Sans:wght@400;600&display=swap">
<style>
:root{
  --blue:#1b73c9;
  --blue-dark:#0f4f94;
  --navy:#142c49;
  --ink:#3a3f47;
  --muted:#8a9099;
  --line:#e3e6ea;
  --footer:#23272c;
  --white:#ffffff;
  --soft:#f5f7f9;
}
*{box-sizing:border-box;margin:0;padding:0}
html,body{width:1200px;height:3400px;overflow:hidden}
body{font-family:"Open Sans",Arial,sans-serif;color:var(--ink);background:var(--white);font-size:14px;line-height:1.6}
h1,h2,h3,h4,.nav,.brand,.btn{font-family:"Montserrat",Arial,sans-serif}
section,header{overflow:hidden}
.section-title{font-size:34px;font-weight:400;text-align:center;color:var(--ink);line-height:1.3}
.section-title strong{color:var(--blue);font-weight:600}
.section-lead{text-align:center;color:var(--muted);font-size:13px;margin-top:8px}
.btn{display:inline-block;background:var(--white);color:var(--blue);font-size:12px;font-weight:600;padding:9px 20px;border-radius:3px}
.more{color:var(--blue);font-size:12px;font-weight:600}

/* hero */
.hero{position:relative;height:560px;background:linear-gradient(180deg,#8fb2d1 0%,#5f83a8 45%,#2f4a6a 100%)}
.hero-photo{position:absolute;inset:0;background:linear-gradient(160deg,#b9d0e4 0%,#6c8fb2 40%,#3b5779 75%,#25384f 100%)}
.topbar{position:absolute;top:0;left:0;right:0;height:90px;background:rgba(255,255,255,.94);display:flex;align-items:center;padding:0 70px;justify-content:space-between}
.brand{font-size:30px;font-weight:700;color:var(--blue);letter-spacing:1px}
.top-right{text-align:right}
.contact-line{font-size:12px;color:var(--muted);display:flex;gap:26px;justify-content:flex-end;margin-bottom:10px}
.contact-line span{display:flex;align-items:center;gap:6px}
.nav{display:flex;gap:34px;font-size:12px;font-weight:600;text-transform:uppercase;color:var(--ink)}
.nav .active{color:var(--blue)}
.hero-copy{position:absolute;left:0;right:0;top:390px;text-align:center;color:var(--white)}
.hero-copy h1{font-size:34px;font-weight:600;text-transform:uppercase;letter-spacing:1px}
.hero-copy p{font-size:15px;text-transform:uppercase;letter-spacing:1px;margin-top:6px}
.hero-curve{position:absolute;left:0;bottom:0;width:1200px;height:70px}

/* steps */
.steps{height:400px;padding-top:50px}
.step-row{display:flex;justify-content:center;gap:110px;margin-top:42px}
.step{width:230px;text-align:center}
.step-icon{width:100px;height:100px;border-radius:50%;background:#6d7177;margin:0 auto 18px;display:flex;align-items:center;justify-content:center;box-shadow:0 0 0 8px #eceef1}
.step.featured .step-icon{background:var(--blue);box-shadow:0 0 0 8px #d6e6f6}
.step h3{font-size:17px;font-weight:600}
.step p{font-size:12px;color:var(--muted);margin-top:6px}

/* about */
.about{height:360px;display:flex}
.about-photo{width:600px;height:360px;background:linear-gradient(135deg,#d9d4cc,#9a8f84 60%,#5d5650)}
.about-panel{width:600px;background:var(--blue);color:var(--white);padding:55px 70px}
.about-panel h2{font-size:28px;font-weight:400}
.about-panel h2 strong{font-weight:700}
.about-panel p{font-size:12px;margin-top:12px;opacity:.92}
.about-panel .btn{margin-top:20px}

/* criteria */
.criteria{height:680px;padding-top:50px}
.criteria-grid{display:grid;grid-template-columns:repeat(3,300px);column-gap:30px;row-gap:22px;justify-content:center;margin-top:36px}
.criterion{text-align:center;padding:22px 20px 20px}
.criterion.featured{box-shadow:0 4px 18px rgba(0,0,0,.12)}
.criterion svg{display:block;margin:0 auto 10px}
.criterion h4{font-size:15px;font-weight:600;color:var(--ink);line-height:1.4}
.criterion.featured h4{color:var(--blue)}
.criterion p{font-size:12px;color:var(--muted);margin:8px 0 10px}

/* newsletter */
.newsletter{position:relative;height:320px;background:linear-gradient(120deg,#1d3a5e,#122640 55%,#0c1b30);color:var(--white);text-align:center;padding-top:60px}
.newsletter h2{font-size:34px;font-weight:400}
.newsletter h2 strong{font-weight:700}
.newsletter .rule{width:60px;height:3px;background:var(--blue);margin:12px auto}
.newsletter p{font-size:13px;opacity:.85}
.signup{width:600px;height:50px;margin:30px auto 0;background:var(--white);border-radius:25px;display:flex;align-items:center;justify-content:space-between;padding-left:24px}
.signup span{color:var(--muted);font-size:13px;display:flex;gap:10px;align-items:center}
.signup .submit{height:50px;padding:0 34px;background:var(--blue);color:var(--white);border-radius:25px;display:flex;align-items:center;gap:10px;font-family:"Montserrat",Arial,sans-serif;font-weight:700;font-size:13px}

/* news */
.news{height:600px;padding-top:50px}
.news-grid{display:flex;gap:40px;width:1000px;margin:36px auto 0}
.news-main{width:520px}
.news-main .thumb{height:290px;background:linear-gradient(135deg,#d6dde5,#8c9cae)}
.news-side{flex:1;display:flex;flex-direction:column;gap:30px}
.news-small{display:flex;gap:22px}
.news-small .thumb{width:190px;height:170px;flex:none;background:linear-gradient(135deg,#e2e4e6,#a7aeb6)}
.news-small .thumb.b{background:linear-gradient(135deg,#c9ccd0,#7c858f)}
.meta{font-size:11px;color:var(--muted);display:flex;gap:16px;margin-top:14px}
.news h3{font-size:17px;font-weight:600;line-height:1.35;margin:8px 0}
.news-small h3{font-size:15px}

/* footer */
.footer{height:420px;background:var(--footer);color:#c7ccd2;padding:60px 100px 0;display:flex;gap:60px}
.footer h4{color:var(--white);font-size:13px;font-weight:600;text-transform:uppercase;margin-bottom:18px}
.footer ul{list-style:none;font-size:12px}
.footer li{margin-bottom:10px;display:flex;gap:10px;align-items:center}
.map{width:220px;height:150px;background:linear-gradient(135deg,#e8e4d8,#c8d6c4)}
.socials{display:flex;gap:10px;margin-bottom:40px}
.socials i{width:30px;height:30px;border-radius:50%;background:var(--blue);display:block}
.footer .brand{font-size:22px;color:var(--white)}
.copyright{height:60px;background:var(--blue);color:var(--white);font-size:12px;text-align:center;line-height:60px}
</style>
</head>
<body>

<header class="hero">
  <div class="hero-photo" role="img" aria-label="City skyline of glass towers seen from a riverside walkway"></div>
  <div class="topbar">
    <div class="brand">Stone Ridge Capital</div>
    <div class="top-right">
      <div class="contact-line">
        <span><svg width="14" height="10" viewBox="0 0 14 10"><rect x=".5" y=".5" width="13" height="9" fill="none" stroke="#1b73c9"/><path d="M.5 .5 7 5.5 13.5 .5" fill="none" stroke="#1b73c9"/></svg>info@stoneridgecapital.com</span>
        <span><svg width="12" height="12" viewBox="0 0 12 12"><path d="M2 1h2.5l1 3-1.5 1a7 7 0 0 0 3 3l1-1.5 3 1V10a1 1 0 0 1-1 1A10 10 0 0 1 1 2a1 1 0 0 1 1-1z" fill="#1b73c9"/></svg>(555) 014-2290</span>
      </div>
      <nav class="nav"><span class="active">Home</span><span>Investment Criteria</span><span>Approach</span><span>Team</span><span>Contact</span></nav>
    </div>
  </div>
  <div class="hero-copy">
    <h1>Whatever your financial goals,</h1>
    <p>We have the experience to get to the truth of your financial wellbeing.</p>
  </div>
  <svg class="hero-curve" viewBox="0 0 1200 70" preserveAspectRatio="none"><path d="M0 40 Q600 80 1200 10 L1200 70 L0 70Z" fill="#1b73c9"/><path d="M0 50 Q600 90 1200 22 L1200 70 L0 70Z" fill="#fff"/></svg>
</header>

<section class="steps">
  <h2 class="section-title">How its <strong>Work</strong></h2>
  <p class="section-lead">Sed ut perspiciatis unde omnis iste natus error sit voluptatem</p>
  <div class="step-row">
    <div class="step">
      <div class="step-icon"><svg width="44" height="44" viewBox="0 0 44 44" fill="none" stroke="#fff" stroke-width="2"><rect x="6" y="8" width="32" height="22" rx="2"/><path d="M16 36h12M22 30v6"/></svg></div>
      <h3>Apply</h3>
      <p>Lorem ipsum dolor sit amet, consectetur adipiscing elit, sed do eiusmod tempor incididunt.</p>
    </div>
    <div class="step featured">
      <div class="step-icon"><svg width="44" height="44" viewBox="0 0 44 44" fill="none" stroke="#fff" stroke-width="2"><rect x="6" y="6" width="32" height="32"/><path d="M13 31V22M20 31V15M27 31V19M34 31V12"/></svg></div>
      <h3>Compare</h3>
      <p>Lorem ipsum dolor sit amet, consectetur adipiscing elit, sed do eiusmod tempor incididunt.</p>
    </div>
    <div class="step">
      <div class="step-icon"><svg width="44" height="44" viewBox="0 0 44 44" fill="none" stroke="#fff" stroke-width="2"><circle cx="22" cy="22" r="15"/><path d="M14 22l6 6 11-12"/></svg></div>
      <h3>Succeed</h3>
      <p>Lorem ipsum dolor sit amet, consectetur adipiscing elit, sed do eiusmod tempor incididunt.</p>
    </div>
  </div>
</section>

<section class="about">
  <div class="about-photo" role="img" aria-label="Team of colleagues reviewing documents together in a bright office"></div>
  <div class="about-panel">
    <h2>About <strong>Stone Ridge Capital</strong></h2>
    <p>Ut enim ad minim veniam, quis nostrud exercitation ullamco laboris nisi ut aliquip ex ea commodo consequat duis aute irure dolor in reprehenderit.</p>
    <p>Lorem ipsum dolor sit amet, consectetur adipiscing elit, sed do eiusmod tempor incididunt ut labore et dolore magna aliqua quis nostrud.</p>
    <p>Excepteur sint occaecat cupidatat non proident, sunt in culpa qui officia deserunt mollit anim id est laborum sed perspiciatis.</p>
    <span class="btn">Read More</span>
  </div>
</section>

<section class="criteria">
  <h2 class="section-title">Our Investment <strong>Criteria</strong></h2>
  <p class="section-lead">Lorem ipsum dolor sit amet, consectetur adipiscing elit, sed do eiusmod tempor incididunt ut labore et dolore.</p>
  <div class="criteria-grid">
    <div class="criterion">
      <svg width="36" height="36" viewBox="0 0 40 40" fill="none" stroke="#1b73c9" stroke-width="2"><circle cx="20" cy="20" r="14"/><path d="M20 11v18M25 15h-7a3 3 0 0 0 0 6h4a3 3 0 0 1 0 6h-7"/></svg>
      <h4>Capacity To Generate Cash Flow</h4>
      <p>Lorem ipsum dolor sit amet, consectetur adipiscing elit sed do eiusmod tempor.</p>
      <span class="more">Read More &rarr;</span>
    </div>
    <div class="criterion featured">
      <svg width="36" height="36" viewBox="0 0 40 40" fill="none" stroke="#1b73c9" stroke-width="2"><circle cx="20" cy="9" r="4"/><path d="M20 13v8M10 21h20M10 21v6M30 21v6M20 21v6"/><circle cx="10" cy="30" r="3"/><circle cx="20" cy="30" r="3"/><circle cx="30" cy="30" r="3"/></svg>
      <h4>Solid Business Model</h4>
      <p>Lorem ipsum dolor sit amet, consectetur adipiscing elit sed do eiusmod tempor.</p>
      <span class="more">Read More &rarr;</span>
    </div>
    <div class="criterion">
      <svg width="36" height="36" viewBox="0 0 40 40" fill="none" stroke="#1b73c9" stroke-width="2"><path d="M5 34h30M9 34V24M17 34V18M25 34V22M33 34V12M7 18l9-7 8 5 11-9"/></svg>
      <h4>Growth Perspective</h4>
      <p>Lorem ipsum dolor sit amet, consectetur adipiscing elit sed do eiusmod tempor.</p>
      <span class="more">Read More &rarr;</span>
    </div>
    <div class="criterion">
      <svg width="36" height="36" viewBox="0 0 40 40" fill="none" stroke="#1b73c9" stroke-width="2"><circle cx="20" cy="12" r="5"/><path d="M10 32a10 10 0 0 1 20 0"/><circle cx="8" cy="16" r="3"/><circle cx="32" cy="16" r="3"/></svg>
      <h4>Strong Management And Governance</h4>
      <p>Lorem ipsum dolor sit amet, consectetur adipiscing elit sed do eiusmod tempor.</p>
      <span class="more">Read More &rarr;</span>
    </div>
    <div class="criterion">
      <svg width="36" height="36" viewBox="0 0 40 40" fill="none" stroke="#1b73c9" stroke-width="2"><circle cx="20" cy="11" r="5"/><path d="M11 34V24a9 9 0 0 1 18 0v10"/><path d="M15 27l4 4 7-8"/></svg>
      <h4>Investor Relevance</h4>
      <p>Lorem ipsum dolor sit amet, consectetur adipiscing elit sed do eiusmod tempor.</p>
      <span class="more">Read More &rarr;</span>
    </div>
    <div class="criterion">
      <svg width="36" height="36" viewBox="0 0 40 40" fill="none" stroke="#1b73c9" stroke-width="2"><rect x="6" y="6" width="28" height="28"/><path d="M11 28l7-8 5 4 8-11"/></svg>
      <h4>Market Potential</h4>
      <p>Lorem ipsum dolor sit amet, consectetur adipiscing elit sed do eiusmod tempor.</p>
      <span class="more">Read More &rarr;</span>
    </div>
  </div>
</section>

<section class="newsletter" role="img" aria-label="Dark blue backdrop of a financial chart on a screen">
  <h2>Sign Up <strong>Our Newsletter</strong></h2>
  <div class="rule"></div>
  <p>Sed ut perspiciatis unde omnis iste natus error sit voluptatem accusantium doloremque laudantium.</p>
  <div class="signup">
    <span><svg width="14" height="10" viewBox="0 0 14 10"><rect x=".5" y=".5" width="13" height="9" fill="none" stroke="#8a9099"/><path d="M.5 .5 7 5.5 13.5 .5" fill="none" stroke="#8a9099"/></svg>Enter Your Email</span>
    <div class="submit">SUBMIT <svg width="14" height="14" viewBox="0 0 14 14"><path d="M1 7 13 1 9 13 7 8z" fill="#fff"/></svg></div>
  </div>
</section>

<section class="news">
  <h2 class="section-title">Latest News <strong>Update</strong></h2>
  <div class="news-grid">
    <article class="news-main">
      <div class="thumb" role="img" aria-label="Business partners shaking hands across a desk"></div>
      <div class="meta"><span>By Admin</span><span>27 March 2019</span></div>
      <h3>Lorem ipsum dolor sit Amet, Elit, sed Eiusmod Tempor Incididunt ut Labore et Dolore</h3>
      <span class="more">Continue Reading &rarr;</span>
    </article>
    <div class="news-side">
      <article class="news-small">
        <div class="thumb" role="img" aria-label="Hands working on a laptop with papers"></div>
        <div>
          <div class="meta"><span>By Admin</span><span>27 March 2019</span></div>
          <h3>Elit, sed Eiusmod Tempor Incididunt ut Labore...</h3>
          <span class="more">Read More &rarr;</span>
        </div>
      </article>
      <article class="news-small">
        <div class="thumb b" role="img" aria-label="Desk with a calculator and financial reports"></div>
        <div>
          <div class="meta"><span>By Admin</span><span>27 March 2019</span></div>
          <h3>Elit, sed Eiusmod Tempor Incididunt</h3>
          <span class="more">Read More &rarr;</span>
        </div>
      </article>
    </div>
  </div>
</section>

<footer>
  <div class="footer">
    <div>
      <h4>Quick Links</h4>
      <ul><li>&rsaquo; Home</li><li>&rsaquo; Approach</li><li>&rsaquo; Investment Criteria</li><li>&rsaquo; Team</li><li>&rsaquo; Contact</li></ul>
    </div>
    <div>
      <h4>Contact Details</h4>
      <ul>
        <li><svg width="12" height="14" viewBox="0 0 12 14"><path d="M6 13S1 8 1 5a5 5 0 0 1 10 0c0 3-5 8-5 8z" fill="#1b73c9"/><circle cx="6" cy="5" r="2" fill="#23272c"/></svg>418 Harbor Lane, Suite 200</li>
        <li><svg width="12" height="14"></svg>Springfield, ST 10020</li>
        <li><svg width="12" height="12" viewBox="0 0 12 12"><path d="M2 1h2.5l1 3-1.5 1a7 7 0 0 0 3 3l1-1.5 3 1V10a1 1 0 0 1-1 1A10 10 0 0 1 1 2a1 1 0 0 1 1-1z" fill="#1b73c9"/></svg>(555) 014-2290</li>
        <li><svg width="12" height="12" viewBox="0 0 12 12"><path d="M2 1h2.5l1 3-1.5 1a7 7 0 0 0 3 3l1-1.5 3 1V10a1 1 0 0 1-1 1A10 10 0 0 1 1 2a1 1 0 0 1 1-1z" fill="#1b73c9"/></svg>(555) 014-2291</li>
        <li><svg width="14" height="10" viewBox="0 0 14 10"><rect x=".5" y=".5" width="13" height="9" fill="none" stroke="#1b73c9"/><path d="M.5 .5 7 5.5 13.5 .5" fill="none" stroke="#1b73c9"/></svg>info@stoneridgecapital.com</li>
      </ul>
    </div>
    <div>
      <h4>Location Map</h4>
      <div class="map" role="img" aria-label="Street map showing the office location"></div>
    </div>
    <div>
      <h4>Follow Us</h4>
      <div class="socials"><i></i><i></i><i></i></div>
      <div class="brand">Stone Ridge Capital</div>
    </div>
  </div>
  <div class="copyright">Copyright &copy; 2019 Stone Ridge Capital. All Rights Reserved.</div>
</footer>

</body>
</html>
```